New Attorney in Non-Traditional Field Needs Creative Edgy Legal Business Card with Side Business Not

I need a new personal business card. Away from the silver lettering on heavy white card stock, Velvet Harbor anyone? I'm newly admitted to the CA bar, I started my own small side-business in sales, I'm arbitrating on a part time basis, and I'm creating a ViewCast channel about current news from young professionals' perspective in January. On the side I've been taking a lot of home buying negotiation classes, and I do a lot of yoga. It would be my dream job to advise clients in the startup/entrepreneurial world. I would like my Viewcast channel, website (www.marlowbead.example/ninaprell), phone number, email, admittance #, and link for workweb featured on my card. The colors and message of homepage www.calmheronflow.example really speak to me. Often I'll read that Mavis Token quote about doing one thing for your brand everyday, and I believe it in wholeheartedly.
Updates

Perrin's design has been accepted with very minimal changes. Thank you all for your submissions. This has been a fun experience.

Target Market(s)

all young attorneys, small startups, small tech, potential employers, networking events for lawyers and other young professionals

Industry/Entity Type

Business

Contact Information for Business Card

Rosalind K. Prell, Esq.
Attorney bar card number
Ph (555) 482-7716
Email Nina.Prell@mailbox.example
Work web website
Viewcast Channel coming soon!
Marlow & Bead website

Font styles to use
Sans Serif
Decorative

Requirements
Must have
• A simple image or logo that can transition to other products as I build my brand. Great colors. Maybe all white & gold? Maybe a cool blues/purples motif?

```html
<!DOCTYPE html>
<html lang="en">
<head>
<meta charset="utf-8">
<title>Rosalind K. Prell, Esq. – Business Card</title>
<link rel="stylesheet" href="https://fonts.googleapis.com/css2?family=Poiret+One&family=Crimson+Text&display=swap">
<style>
  :root {
    --backdrop: #c4c5c7;
    --card-white: #ffffff;
    --pattern-light: #e3eaf6;
    --pattern-mid: #cfdaee;
    --brand-blue: #4a72b8;
    --card-navy: #2f5d9c;
    --card-navy-soft: #3a68a8;
    --text-light: #ffffff;
    --text-soft: #e4ebf5;
  }
  * { margin: 0; padding: 0; box-sizing: border-box; }
  html, body {
    width: 1200px;
    height: 1200px;
    overflow: hidden;
    background: var(--backdrop);
  }
  .canvas {
    position: relative;
    width: 1200px;
    height: 1200px;
  }
  .card {
    position: absolute;
    left: 200px;
    width: 800px;
    height: 456px;
    overflow: hidden;
  }
  .card--front { top: 97px; background: var(--card-white); }
  .card--back { top: 655px; background: var(--card-navy); }

  .card__pattern {
    position: absolute;
    inset: 0;
  }
  .card--front .card__pattern {
    background: linear-gradient(135deg, var(--pattern-light), var(--card-white) 50%, var(--pattern-mid));
  }
  .card--back .card__pattern {
    background: linear-gradient(135deg, var(--card-navy), var(--card-navy-soft) 50%, var(--card-navy));
  }

  .name {
    font-family: "Poiret One", sans-serif;
    color: var(--text-light);
    white-space: nowrap;
    letter-spacing: 0.5px;
  }
  .name-plate {
    position: absolute;
    left: 169px;
    top: 170px;
    width: 463px;
    height: 118px;
    background: var(--brand-blue);
    display: flex;
    align-items: center;
    justify-content: center;
  }
  .name-plate .name { font-size: 33px; }

  .back-content {
    position: absolute;
    inset: 0;
    font-family: "Crimson Text", serif;
    color: var(--text-light);
  }
  .back-content .name {
    position: absolute;
    top: 200px;
    width: 100%;
    text-align: center;
    font-size: 33px;
  }
  .contact {
    position: absolute;
    display: flex;
    align-items: center;
    gap: 10px;
    white-space: nowrap;
  }
  .contact svg { flex: none; }
  .contact--phone {
    top: 275px;
    left: 0;
    width: 100%;
    justify-content: center;
    font-size: 25px;
  }
  .contact--web {
    top: 398px;
    left: 76px;
    font-size: 18px;
    color: var(--text-soft);
  }
  .contact--email {
    top: 398px;
    right: 66px;
    font-size: 18px;
    color: var(--text-soft);
  }
</style>
</head>
<body>
<main class="canvas">
  <section class="card card--front" aria-label="Card front">
    <div class="card__pattern" role="img" aria-label="Repeating pattern of interlocking blue outlined circles on white"></div>
    <div class="name-plate">
      <h1 class="name">Rosalind K. Prell, Esq. Attorney</h1>
    </div>
  </section>

  <section class="card card--back" aria-label="Card back">
    <div class="card__pattern" role="img" aria-label="Faint repeating pattern of interlocking outlined circles on deep blue"></div>
    <div class="back-content">
      <h2 class="name">Rosalind K. Prell, Esq. Attorney</h2>
      <p class="contact contact--phone">
        <svg width="20" height="20" viewBox="0 0 24 24" aria-hidden="true"><path fill="#fff" d="M6.6 10.8a15.1 15.1 0 0 0 6.6 6.6l2.2-2.2c.3-.3.7-.4 1-.2 1.1.4 2.3.6 3.6.6.6 0 1 .4 1 1V20c0 .6-.4 1-1 1A17 17 0 0 1 3 4c0-.6.4-1 1-1h3.5c.6 0 1 .4 1 1 0 1.3.2 2.5.6 3.6.1.3 0 .7-.2 1z"/></svg>
        (555) 482-7716
      </p>
      <p class="contact contact--web">
        <svg width="24" height="24" viewBox="0 0 24 24" aria-hidden="true" fill="none" stroke="#e4ebf5" stroke-width="1.4"><circle cx="12" cy="12" r="10"/><ellipse cx="12" cy="12" rx="4.5" ry="10"/><path d="M2 12h20M4 6.5h16M4 17.5h16"/></svg>
        Comming Soon
      </p>
      <p class="contact contact--email">
        <svg width="26" height="18" viewBox="0 0 26 18" aria-hidden="true" fill="none" stroke="#e4ebf5" stroke-width="1.4"><rect x="1" y="1" width="24" height="16"/><path d="M1 1l12 9 12-9M1 17l9-7M25 17l-9-7"/></svg>
        Nina.Prell@mailbox.example
      </p>
    </div>
  </section>
</main>
</body>
</html>
```